A register your interest postcard

It is a slightly bigger postcard that wil be inserted inside a brochure. On one side it is to have the logo with the statement "at Corvanne, Byron Bay" underneath. At the bottom it is to say "Register your interest to become an owner at The Keyholders Circle. On the flipside it has the logo in a smaller version with again in smaller writing "Become an owner at The Keyholders Circle". The main point of this side it to say " SMS your name to 0491 562 037 OR Name: Email: Phone:".
I would like a wood-look style postcard. It is for a luxury beach property that uses a lot of distressed wood in the building of the houses.
Industry/Entity Type
Building
Contact Information for Business Card
I would like a wood-look style postcard for a beach property.
Look and feel
Each slider illustrates characteristics of the customer's brand and the style your logo design should communicate.

```html
<!DOCTYPE html>
<html lang="en">
<head>
<meta charset="utf-8">
<title>The Keyholders Circle – Register Your Interest Postcard</title>
<link href="https://fonts.googleapis.com/css2?family=Poppins:wght@600;700&display=swap" rel="stylesheet">
<style>
  :root {
    --wood-light: #c9a57a;
    --wood-mid: #b08a5e;
    --wood-dark: #8c6a45;
    --ink: #111111;
    --paper: #ffffff;
    --band: #0f4a5e;
    --trim: #d9534f;
  }
  * { margin: 0; padding: 0; box-sizing: border-box; }
  html, body {
    width: 1200px;
    height: 741px;
    overflow: hidden;
    background: var(--paper);
  }
  .postcard {
    position: relative;
    width: 1200px;
    height: 741px;
    background: var(--paper);
    font-family: "Poppins", "Century Gothic", sans-serif;
  }
  .wood-surface {
    position: absolute;
    left: 0;
    top: 0;
    width: 1200px;
    height: 632px;
    background: linear-gradient(172deg, var(--wood-light) 0%, var(--wood-mid) 45%, var(--wood-light) 70%, var(--wood-dark) 100%);
  }
  .trim-guide {
    position: absolute;
    left: 20px;
    top: 20px;
    width: 1160px;
    height: 700px;
    border: 1px dashed var(--trim);
    opacity: 0.7;
    pointer-events: none;
  }
  .brand-name {
    position: absolute;
    left: 50px;
    top: 46px;
    color: var(--ink);
    font-weight: 700;
    font-size: 94px;
    line-height: 113px;
    letter-spacing: 2px;
    text-transform: uppercase;
  }
  .location {
    position: absolute;
    left: 50px;
    top: 400px;
    color: var(--paper);
    font-weight: 700;
    font-size: 45px;
    letter-spacing: 0.5px;
  }
  .cta-band {
    position: absolute;
    left: 20px;
    top: 630px;
    width: 1160px;
    height: 91px;
    background: var(--band);
    display: flex;
    align-items: center;
    justify-content: center;
  }
  .cta-text {
    color: var(--paper);
    font-weight: 600;
    font-size: 32px;
  }
</style>
</head>
<body>
  <main class="postcard">
    <div class="wood-surface" role="img" aria-label="Close-up photograph of weathered, distressed timber planks"></div>
    <h1 class="brand-name">The<br>Keyholders<br>Circle</h1>
    <p class="location">at Corvanne, Byron Bay</p>
    <div class="cta-band">
      <p class="cta-text">Register your interest to become an owner at The Keyholders Circle.</p>
    </div>
    <div class="trim-guide" aria-hidden="true"></div>
  </main>
</body>
</html>
```